Builders Worksite Corflute Outdoor Sign

We are a building company who are just branching out into new construction. How first new build is our own home which was designed by us and a local architect. We are proud and want to create more advertisement around our business.

We need a corflute sign that can staked outside the construction site and can be seen by people passing by.
Updates

Can we please make the company name and logo bigger (Tidewater Lane Homes) This needs to be the focus. Can we please replace 'Mako' with 'Contact Us on 021-649-3157'

Target Market(s)

Home owners and people wishing to build on lifestyle blocks in New Zealand.

Font styles to use
Sans Serif

Requirements
Must have
• It needs to feature our:
Logo
Company name
Contact name and number - Mako - 0216493157
Landscape NOT portrait.

```html
<!DOCTYPE html>
<html lang="en">
<head>
<meta charset="utf-8">
<title>Tidewater Lane Homes – Site Sign</title>
<link rel="stylesheet" href="https://fonts.googleapis.com/css2?family=Anton&family=Josefin+Sans:wght@300&family=Montserrat:wght@800&display=swap">
<style>
  :root {
    --page: #ffffff;
    --charcoal: #262626;
    --paper: #ffffff;
    --navy: #141d2e;
    --gold: #e2aa2a;
    --white: #ffffff;
  }
  * { box-sizing: border-box; margin: 0; padding: 0; }
  html, body {
    width: 900px;
    height: 1200px;
    overflow: hidden;
    background: var(--page);
  }
  .canvas {
    width: 900px;
    height: 1200px;
    display: flex;
    align-items: center;
    justify-content: center;
  }
  .sign {
    width: 820px;
    height: 612px;
    display: flex;
    flex-direction: column;
    box-shadow: 2px 3px 4px rgba(0,0,0,0.35);
    background: var(--paper);
  }
  .brand-panel {
    height: 356px;
    background: var(--charcoal);
    display: flex;
    flex-direction: column;
    align-items: center;
    justify-content: center;
    color: var(--white);
    font-family: "Josefin Sans", sans-serif;
    font-weight: 300;
  }
  .brand-name {
    font-size: 72px;
    line-height: 1;
    letter-spacing: 1px;
  }
  .brand-sub {
    margin-top: 34px;
    font-size: 50px;
    line-height: 1;
    letter-spacing: 30px;
    padding-left: 30px;
  }
  .info-panel {
    flex: 1;
    display: flex;
    flex-direction: column;
    align-items: center;
    justify-content: center;
    gap: 22px;
  }
  .headline {
    font-family: "Anton", sans-serif;
    font-weight: 400;
    font-size: 80px;
    line-height: 1;
    color: var(--navy);
    letter-spacing: -1px;
  }
  .headline .accent { color: var(--gold); }
  .contact-bar {
    position: relative;
    width: 690px;
    height: 80px;
  }
  .contact-shapes {
    position: absolute;
    left: 0; top: 0;
  }
  .contact-name,
  .contact-phone {
    position: absolute;
    top: 10px;
    height: 60px;
    display: flex;
    align-items: center;
    justify-content: center;
    font-family: "Montserrat", sans-serif;
    font-weight: 800;
    color: var(--white);
    line-height: 1;
  }
  .contact-name {
    left: 0;
    width: 180px;
    font-size: 40px;
    letter-spacing: 1px;
  }
  .contact-phone {
    left: 250px;
    width: 430px;
    gap: 18px;
    font-size: 42px;
    letter-spacing: 1px;
  }
</style>
</head>
<body>
<main class="canvas">
  <section class="sign">
    <header class="brand-panel">
      <div class="brand-name">TIDEWATER LANE</div>
      <div class="brand-sub">HOMES</div>
    </header>
    <div class="info-panel">
      <h1 class="headline">TIDEWATER <span class="accent">LANE</span> HOMES</h1>
      <div class="contact-bar">
        <svg class="contact-shapes" width="690" height="80" viewBox="0 0 690 80" aria-hidden="true">
          <path fill="#141d2e" d="M190,10 H682 Q690,10 690,18 V62 Q690,70 682,70 H190 L222,40 Z"/>
          <path fill="#e2aa2a" d="M6,10 H180 V70 H6 Q0,70 0,64 V16 Q0,10 6,10 Z"/>
          <polygon points="176,0 238,40 176,80" fill="#e2aa2a" stroke="#ffffff" stroke-width="3" stroke-linejoin="miter"/>
          <rect x="170" y="10" width="8" height="60" fill="#e2aa2a"/>
        </svg>
        <div class="contact-name">MAKO</div>
        <div class="contact-phone">
          <svg width="34" height="34" viewBox="0 0 24 24" aria-hidden="true">
            <path fill="#ffffff" d="M6.6 10.8a15.1 15.1 0 0 0 6.6 6.6l2.2-2.2c.3-.3.7-.4 1-.2 1.1.4 2.3.6 3.6.6.6 0 1 .4 1 1V20c0 .6-.4 1-1 1A17 17 0 0 1 3 4c0-.6.4-1 1-1h3.5c.6 0 1 .4 1 1 0 1.3.2 2.5.6 3.6.1.3 0 .7-.2 1z"/>
            <path fill="none" stroke="#ffffff" stroke-width="1.8" stroke-linecap="round" d="M14 3.5a6.5 6.5 0 0 1 6.5 6.5M14 7a3 3 0 0 1 3 3"/>
          </svg>
          <span>0216493157</span>
        </div>
      </div>
    </div>
  </section>
</main>
</body>
</html>
```